Business Card for Makeup Artist

I need a business card designed for my makeup and hair artistry business which is primarily events and weddings focused. The card needs to be sleek, simple, stylish and appealing to women. I would prefer a white background but open to suggestions also. I also love the marble background look. I have attached some example pics. It needs to be a double sided card with logo and/or design on one side and contact details in the centre of the card on the other side. NO LOGO ON BACK. Examples attached.

Target Market(s)

Females age 14-55

Industry/Entity Type

Business

Contact Information for Business Card

Nora Vint
Principal Makeup Artist
P: 0413 925 214
E: nora@lumirabeauty.com.au
W: www.lumirabeauty.com.au

Requirements
Should not have
• No yellow, green, red or blue in the design.

```html
<!DOCTYPE html>
<html lang="en">
<head>
<meta charset="utf-8">
<title>Lumira Makeup Artistry – Business Card</title>
<link rel="stylesheet" href="https://fonts.googleapis.com/css2?family=Kalam:wght@400;700&display=swap">
<style>
  :root {
    --stage: #5b5b5d;
    --card: #ffffff;
    --ink: #5a5a5c;
    --rose: #d96aa8;
    --slate: #5f5f61;
    --rule: #8a8a8c;
  }
  * { margin: 0; padding: 0; box-sizing: border-box; }
  html, body { width: 1200px; height: 800px; overflow: hidden; }
  body {
    position: relative;
    background: var(--stage);
    font-family: "Kalam", cursive;
    color: var(--ink);
  }
  .card {
    position: absolute;
    width: 560px;
    height: 312px;
    background: var(--card);
    box-shadow: 0 4px 10px rgba(0,0,0,0.35);
    overflow: hidden;
  }
  .card--front { left: 180px; top: 64px; }
  .card--back  { left: 460px; top: 424px; }

  .card__bands {
    position: absolute;
    left: 0; bottom: 0;
    width: 560px; height: 44px;
    display: block;
  }

  .brand-name {
    position: absolute;
    left: 0; width: 100%;
    top: 108px;
    text-align: center;
    font-weight: 400;
    color: var(--ink);
    white-space: nowrap;
    line-height: 1;
  }
  .brand-name__word { display: block; font-size: 58px; }
  .brand-name__trade { display: block; font-size: 20px; margin-top: 4px; letter-spacing: 1px; }

  .divider {
    position: absolute;
    left: 289px;
    top: 51px;
    width: 2px;
    height: 210px;
    background: var(--rule);
  }

  .contact {
    position: absolute;
    left: 306px;
    top: 80px;
    font-weight: 700;
    color: var(--ink);
    white-space: nowrap;
  }
  .contact__name { font-size: 28px; line-height: 1.1; letter-spacing: 1px; }
  .contact__role { font-size: 15px; line-height: 1.2; margin-top: 10px; }
  .contact__list { list-style: none; margin-top: 18px; }
  .contact__list li { font-size: 14px; line-height: 25px; }
  .contact__list li.small { font-size: 12px; }
</style>
</head>
<body>

  <section class="card card--front" aria-label="Card front">
    <p class="brand-name">
      <span class="brand-name__word">Lumira</span>
      <span class="brand-name__trade">Makeup Artistry</span>
    </p>
    <svg class="card__bands" viewBox="0 0 560 44" aria-hidden="true">
      <polygon points="0,0 292,0 312,22 0,22" fill="var(--rose)"/>
      <rect x="0" y="22" width="560" height="22" fill="var(--slate)"/>
    </svg>
  </section>

  <section class="card card--back" aria-label="Card back">
    <div class="divider"></div>
    <div class="contact">
      <p class="contact__name">Nora Vint</p>
      <p class="contact__role">Principal Makeup Artist</p>
      <ul class="contact__list">
        <li>0413 925 214</li>
        <li class="small">nora@lumirabeauty.com.au</li>
        <li class="small">www.lumirabeauty.com.au</li>
      </ul>
    </div>
    <svg class="card__bands" viewBox="0 0 560 44" aria-hidden="true">
      <polygon points="0,0 290,0 312,22 0,22" fill="var(--rose)"/>
      <rect x="0" y="22" width="560" height="22" fill="var(--slate)"/>
    </svg>
  </section>

</body>
</html>
```